QM_radiance is a new upcoming amazing brand for modesty women , which started in 2016.

Design a page with all products and stating the title of the collection and style of the products and pricing.
Will need to create a column of upcoming events as well for customer to keep updated of our sales or flea
Updates

Target Market(s)

Hijabista, modesttrend

Number of Pages Required

5+ page

Requirements
Nice to have
• About Us
• Our brand represents classy and elegance yet it is comfortable and conservative to be worn everyday.
• Designs, and colours of fabrics chiffon , silk crepe and sateen silks and viscose cotton are exclusively chosen by QMradiance, imported from mainly high quality materials and sent for self manufactured.
• InsyaAllah#QMradiance

```html
<!DOCTYPE html>
<html lang="en">
<head>
<meta charset="utf-8">
<title>QM Radiance – Modest Fashion</title>
<link rel="stylesheet" href="https://fonts.googleapis.com/css2?family=Roboto:ital,wght@0,300;0,400;0,500;0,700;1,400&family=Oswald:wght@400;500&display=swap">
<style>
:root{
  --teal:#4db2a9;
  --ink:#2b2b2b;
  --muted:#777;
  --red:#d8363b;
  --topbar:#f1f1f1;
  --page:#f3f3f3;
  --card:#ffffff;
  --footer:#3a3a3a;
  --footer-base:#131313;
}
*{box-sizing:border-box;margin:0;padding:0}
html,body{width:1200px;height:2719px;overflow:hidden}
body{font-family:'Roboto',Arial,sans-serif;color:var(--ink);background:var(--page)}
.page{position:relative;width:1200px;height:2719px;overflow:hidden;background:var(--page)}
.abs{position:absolute}

.topbar{left:0;top:0;width:1200px;height:49px;background:var(--topbar);font-size:12px;color:var(--muted)}
.topbar .lang{left:87px;top:17px}
.topbar .lang b{color:var(--ink);font-weight:400}
.topbar .links{right:89px;top:17px}
.topbar .links span{margin:0 10px;color:#bbb}

.header{left:0;top:49px;width:1200px;height:136px;background:#fff}
.circle-icon{width:43px;height:43px;border:1px solid #cfcfcf;border-radius:50%;display:flex;align-items:center;justify-content:center}
.header .phone{left:89px;top:48px}
.header .phone-text{left:141px;top:60px;font-size:15px;color:#444}
.header .cart{left:921px;top:44px}
.header .cart-text{left:973px;top:56px;font-size:14px;color:#444}
.brand{left:0;width:1200px;top:24px;text-align:center}
.brand .mark{display:inline-block;width:46px;height:46px;border:2px solid #222}
.brand .name{display:block;margin-top:8px;font-size:19px;font-weight:500;color:#222}

.nav{left:0;top:185px;width:1200px;height:62px;background:linear-gradient(#3a3a3a,#0e0e0e)}
.nav .active{left:87px;top:0;width:174px;height:62px;background:var(--teal)}
.nav a{position:absolute;top:22px;transform:translateX(-50%);color:#fff;font-size:14px;text-decoration:none;text-transform:uppercase;white-space:nowrap}

.hero{left:0;top:247px;width:1200px;height:592px;background:#fff}
.hero .panel{top:0;height:592px}
.hero .p1{left:0;width:390px;background:linear-gradient(135deg,#f7d6c4,#f1bca8 40%,#2a2422 75%,#1a1a1a)}
.hero .p2{left:395px;width:395px;background:linear-gradient(180deg,#dcdde2 0%,#cfd1d8 30%,#3a3e52 55%,#2c3044 100%)}
.hero .p3{left:794px;width:406px;background:linear-gradient(135deg,#3a3a2c,#b8b48a 40%,#2a2a22 70%,#141414)}
.hero .caption{left:395px;top:447px;width:395px;height:145px;background:rgba(80,80,80,.85);text-align:center;font-family:'Oswald',sans-serif}
.hero .caption .off{color:var(--teal);font-size:44px;line-height:52px;margin-top:16px;letter-spacing:.5px}
.hero .caption .title{color:#fff;font-size:33px;line-height:42px}
.hero .arrow{top:284px;width:32px;height:32px;border-radius:50%;background:rgba(60,60,60,.8);display:flex;align-items:center;justify-content:center}

.tile{top:899px;width:314px;height:216px}
.tile .thumbs{display:flex;gap:6px;height:149px}
.tile .thumb{flex:1}
.tile .bar{position:absolute;left:0;top:152px;width:100%;height:64px;background:#000;display:flex;align-items:center;justify-content:center}
.tile .bar.teal{background:var(--teal)}
.tile .btn{border:1.5px solid #fff;color:#fff;font-size:15px;padding:9px 24px;text-transform:uppercase;letter-spacing:.3px;white-space:nowrap}

.sec-title{font-size:20px;font-weight:400;text-transform:uppercase;color:var(--ink)}
.sec-title em{font-style:normal;color:var(--teal)}
.pager{display:flex;gap:8px}

.s-card{top:1236px;width:243px;height:376px;background:var(--card);border:1px solid #e2e2e2;box-shadow:0 2px 4px rgba(0,0,0,.12);text-align:center}
.s-card .img{position:absolute;left:16px;top:18px;width:211px;height:252px}
.s-card .name{position:absolute;left:0;width:100%;top:297px;font-size:15px;color:#333}
.s-card .price{position:absolute;left:0;width:100%;top:327px;font-size:17px;color:var(--red)}

.a-card{top:1728px;width:242px;height:335px;background:var(--card);border:1px solid #e2e2e2}
.a-card .img{height:208px}
.a-card .name{height:36px;background:#efefef;text-align:center;font-size:15px;line-height:36px;color:#333}
.a-card .price{height:46px;text-align:center;line-height:46px;font-size:17px;color:var(--red)}
.a-card .price s{color:#999;font-size:13px;margin-right:10px}
.a-card .actions{display:flex;height:45px;border-top:1px solid #e3e3e3}
.a-card .actions div{flex:1;display:flex;align-items:center;justify-content:center;border-right:1px solid #e3e3e3}
.a-card .actions div:last-child{border-right:none}
.a-card .actions .buy{background:var(--teal)}
.promo{left:866px;top:1722px;width:245px;height:332px;background:linear-gradient(160deg,#f2f2f0 0%,#c9c6c0 35%,#c0262c 60%,#8f1a1f 100%)}
.promo .best{left:14px;top:148px;font-family:'Oswald',sans-serif;font-size:27px;color:#fff;text-shadow:0 1px 3px rgba(0,0,0,.4)}
.promo .badge{left:120px;top:178px;width:100px;height:100px;border-radius:50%;background:#fff;border:4px solid #e8e8e8;text-align:center;font-family:'Oswald',sans-serif;color:var(--teal);padding-top:22px;line-height:24px;font-size:20px}

.testimonials{left:0;top:2112px;width:1200px;height:299px;background:linear-gradient(120deg,#f7f7f7,#ececec 50%,#f6f6f6)}
.testimonials h2{position:absolute;top:46px;width:100%;text-align:center;font-size:20px;font-weight:400;color:var(--teal);text-transform:uppercase}
.quote{top:114px;width:440px;height:110px}
.quote .avatar{position:absolute;left:0;top:4px;width:84px;height:84px;border-radius:50%;border:3px solid #fff;box-shadow:0 1px 3px rgba(0,0,0,.2)}
.quote .body{position:absolute;left:112px;top:0;width:315px}
.quote .mark{position:absolute;font-family:Georgia,serif;font-size:30px;line-height:30px;color:#999}
.quote p{font-size:12px;font-style:italic;line-height:22px;color:#555;padding-left:14px;padding-right:18px}
.quote .who{margin-top:10px;padding-left:14px;font-size:12px;font-weight:500;color:#333;text-transform:uppercase}
.quote .role{padding-left:14px;margin-top:6px;font-size:12px;font-style:italic;color:#777}

.footer{left:0;top:2411px;width:1200px;height:223px;background:var(--footer);color:#fff}
.footer .col{position:absolute;top:45px}
.footer h4{font-size:15px;font-weight:500;text-transform:uppercase;margin-bottom:20px}
.footer li{list-style:none;font-size:13px;line-height:25px;color:#eee}
.footer .info{font-size:12px;line-height:24px;color:#eee}
.footer .newsletter p{font-size:12px;line-height:18px;width:205px;color:#eee}
.footer .form{display:flex;margin-top:14px}
.footer .form .field{width:142px;height:30px;background:#fff;color:#999;font-size:11px;line-height:30px;padding-left:12px}
.footer .form .submit{width:61px;height:30px;background:var(--teal);font-size:12px;line-height:30px;text-align:center}
.footer .social{display:flex;gap:14px;margin-top:20px}
.footer .social span{width:34px;height:34px;border:1.5px solid #ddd;border-radius:50%;display:block}
.base{left:0;top:2634px;width:1200px;height:85px;background:var(--footer-base)}
.base .cards{left:89px;top:27px;display:flex;gap:4px}
.base .cards span{width:40px;height:27px;border-radius:2px;background:#d8d8d8}
.base .cards span:nth-child(2){background:#e8b04a}
.base .cards span:nth-child(3){background:#2a5aa8}
.base .cards span:nth-child(4){background:#f0f0f0}
.base .cards span:nth-child(5){background:#3f86c6}
.base .copy{right:94px;top:35px;font-size:12px;color:#fff}
</style>
</head>
<body>
<div class="page">

  <div class="abs topbar">
    <div class="abs lang">Language: <b>English</b> ⌄</div>
    <div class="abs links">Sign In or Register<span>|</span>My Account<span>|</span>Add To Wishlist</div>
  </div>

  <header class="abs header">
    <div class="abs circle-icon phone">
      <svg width="18" height="18" viewBox="0 0 24 24"><path fill="#4db2a9" d="M6.6 10.8a15.1 15.1 0 0 0 6.6 6.6l2.2-2.2c.3-.3.7-.4 1-.2 1.1.4 2.3.6 3.6.6.6 0 1 .4 1 1V20c0 .6-.4 1-1 1A17 17 0 0 1 3 4c0-.6.4-1 1-1h3.5c.6 0 1 .4 1 1 0 1.3.2 2.5.6 3.6.1.3 0 .7-.2 1z"/></svg>
    </div>
    <div class="abs phone-text">+61 420 715 3398</div>
    <div class="abs brand"><span class="mark"></span><span class="name">QM Radiance</span></div>
    <div class="abs circle-icon cart">
      <svg width="20" height="20" viewBox="0 0 24 24"><path fill="#4db2a9" d="M7 18a2 2 0 1 0 0 4 2 2 0 0 0 0-4zm10 0a2 2 0 1 0 0 4 2 2 0 0 0 0-4zM5.2 4H2V2h4.5l.9 2H21l-3.2 8H8.4l-.9 2H19v2H4.3l2.3-4.6z"/></svg>
    </div>
    <div class="abs cart-text">SHOPPING CARD : 0</div>
  </header>

  <nav class="abs nav">
    <div class="abs active"></div>
    <a style="left:174px">Trending Now</a>
    <a style="left:326px">Products</a>
    <a style="left:471px">Collections</a>
    <a style="left:600px">Order</a>
    <a style="left:707px">Gifts</a>
    <a style="left:823px">About Us</a>
    <a style="left:955px">Contacts</a>
    <a style="left:1069px">Sale</a>
  </nav>

  <section class="abs hero">
    <div class="abs panel p1" role="img" aria-label="Side view of a model wearing a peach floral chiffon hijab"></div>
    <div class="abs panel p2" role="img" aria-label="Model in a full-length navy sequin dress with a purple hijab"></div>
    <div class="abs panel p3" role="img" aria-label="Side view of a model wearing a dark floral print hijab"></div>
    <div class="abs caption">
      <div class="off">FLAT 35% OFF</div>
      <div class="title">FLOWER BEADS COLLECTION</div>
    </div>
    <div class="abs arrow" style="left:53px"><svg width="12" height="12" viewBox="0 0 12 12"><path d="M8 1L3 6l5 5" fill="none" stroke="#fff" stroke-width="2"/></svg></div>
    <div class="abs arrow" style="left:1115px"><svg width="12" height="12" viewBox="0 0 12 12"><path d="M4 1l5 5-5 5" fill="none" stroke="#fff" stroke-width="2"/></svg></div>
  </section>

  <div class="abs tile" style="left:87px">
    <div class="thumbs">
      <div class="thumb" role="img" aria-label="Model in a dark purple hijab" style="background:linear-gradient(#d9dbe2,#5a2c4e 60%,#f3f3f3)"></div>
      <div class="thumb" role="img" aria-label="Model in a magenta hijab" style="background:linear-gradient(#d9dbe2,#b2267a 60%,#f3f3f3)"></div>
      <div class="thumb" role="img" aria-label="Model in a rose pink hijab" style="background:linear-gradient(#d9dbe2,#c9587a 60%,#f3f3f3)"></div>
    </div>
    <div class="bar"><span class="btn">Sparkle Collection</span></div>
  </div>
  <div class="abs tile" style="left:439px">
    <div class="thumbs">
      <div class="thumb" role="img" aria-label="Model in an olive hijab" style="background:linear-gradient(#d9dbe2,#7a6a22 60%,#f3f3f3)"></div>
      <div class="thumb" role="img" aria-label="Model in a dark green hijab" style="background:linear-gradient(#d9dbe2,#1e4e3a 60%,#f3f3f3)"></div>
      <div class="thumb" role="img" aria-label="Model in a teal hijab" style="background:linear-gradient(#d9dbe2,#3b8c80 60%,#f3f3f3)"></div>
    </div>
    <div class="bar teal"><span class="btn">Crystal Collection</span></div>
  </div>
  <div class="abs tile" style="left:798px">
    <div class="thumbs">
      <div class="thumb" role="img" aria-label="Model in a white hijab" style="background:linear-gradient(#d9dbe2,#ecebf1 60%,#f3f3f3)"></div>
      <div class="thumb" role="img" aria-label="Model in a lilac hijab" style="background:linear-gradient(#d9dbe2,#c8a2d6 60%,#f3f3f3)"></div>
      <div class="thumb" role="img" aria-label="Model in a crimson hijab" style="background:linear-gradient(#d9dbe2,#a8142a 60%,#f3f3f3)"></div>
    </div>
    <div class="bar"><span class="btn">Flower Beads Collection</span></div>
  </div>

  <h2 class="abs sec-title" style="left:94px;top:1190px">Summer <em>Collection</em></h2>
  <div class="abs pager" style="left:1077px;top:1190px">
    <svg width="12" height="18" viewBox="0 0 12 18"><path d="M9 2L3 9l6 7" fill="none" stroke="#222" stroke-width="2.5"/></svg>
    <svg width="12" height="18" viewBox="0 0 12 18"><path d="M3 2l6 7-6 7" fill="none" stroke="#222" stroke-width="2.5"/></svg>
  </div>

  <div class="abs s-card" style="left:91px">
    <div class="img" role="img" aria-label="Model in an olive satin hijab" style="background:linear-gradient(#e4e4ea,#6b6a1c 45%,#1f2330)"></div>
    <div class="name">Neque porro quisquam</div><div class="price">$ 651.00</div>
  </div>
  <div class="abs s-card" style="left:350px">
    <div class="img" role="img" aria-label="Model in a peach floral hijab" style="background:linear-gradient(#e4e4ea,#f0c2ae 45%,#1c1c1c)"></div>
    <div class="name">Neque porro quisquam</div><div class="price">$ 651.00</div>
  </div>
  <div class="abs s-card" style="left:607px">
    <div class="img" role="img" aria-label="Model in a dark floral hijab" style="background:linear-gradient(#e4e4ea,#5e5a42 45%,#1c1c1c)"></div>
    <div class="name">Neque porro quisquam</div><div class="price">$ 651.00</div>
  </div>
  <div class="abs s-card" style="left:866px">
    <div class="img" role="img" aria-label="Model in a cream floral hijab" style="background:linear-gradient(#e4e4ea,#e9ddc9 45%,#1c1c1c)"></div>
    <div class="name">Neque porro quisquam</div><div class="price">$ 651.00</div>
  </div>

  <h2 class="abs sec-title" style="left:91px;top:1685px">Latest <em>Arrivals</em></h2>
  <div class="abs pager" style="left:817px;top:1685px">
    <svg width="12" height="18" viewBox="0 0 12 18"><path d="M9 2L3 9l6 7" fill="none" stroke="#222" stroke-width="2.5"/></svg>
    <svg width="12" height="18" viewBox="0 0 12 18"><path d="M3 2l6 7-6 7" fill="none" stroke="#222" stroke-width="2.5"/></svg>
  </div>

  <div class="abs a-card" style="left:92px">
    <div class="img" role="img" aria-label="Folded teal scarf with flower beads" style="background:linear-gradient(135deg,#ececf0,#3aa898 45%,#2f9687 70%,#ececf0)"></div>
    <div class="name">Lorem ipsum dolor</div>
    <div class="price"><s>$160.00</s>$ 150.00</div>
    <div class="actions">
      <div class="buy"><svg width="18" height="18" viewBox="0 0 24 24"><path fill="#fff" d="M7 18a2 2 0 1 0 0 4 2 2 0 0 0 0-4zm10 0a2 2 0 1 0 0 4 2 2 0 0 0 0-4zM5.2 4H2V2h4.5l.9 2H21l-3.2 8H8.4l-.9 2H19v2H4.3l2.3-4.6z"/></svg></div>
      <div><svg width="16" height="16" viewBox="0 0 24 24"><path fill="#bbb" d="M12 21l-1.5-1.3C5 15 2 12.2 2 8.5 2 5.4 4.4 3 7.5 3c1.7 0 3.4.8 4.5 2.1C13.1 3.8 14.8 3 16.5 3 19.6 3 22 5.4 22 8.5c0 3.7-3 6.5-8.5 11.2z"/></svg></div>
      <div><svg width="16" height="16" viewBox="0 0 24 24"><path d="M4 8h14l-3-3M20 16H6l3 3" fill="none" stroke="#999" stroke-width="2"/></svg></div>
      <div><svg width="16" height="16" viewBox="0 0 24 24"><circle cx="12" cy="12" r="8" fill="none" stroke="#999" stroke-width="2"/><path d="M12 8v5" stroke="#999" stroke-width="2"/></svg></div>
    </div>
  </div>
  <div class="abs a-card" style="left:350px">
    <div class="img" role="img" aria-label="Fan of scarves in many colours" style="background:linear-gradient(135deg,#ececf0 10%,#e94b5a 30%,#f2c531 45%,#3fb06a 60%,#4a7bd1 75%,#ececf0 90%)"></div>
    <div class="name">Lorem ipsum dolor</div>
    <div class="price"><s>$160.00</s>$ 150.00</div>
    <div class="actions">
      <div class="buy"><svg width="18" height="18" viewBox="0 0 24 24"><path fill="#fff" d="M7 18a2 2 0 1 0 0 4 2 2 0 0 0 0-4zm10 0a2 2 0 1 0 0 4 2 2 0 0 0 0-4zM5.2 4H2V2h4.5l.9 2H21l-3.2 8H8.4l-.9 2H19v2H4.3l2.3-4.6z"/></svg></div>
      <div><svg width="16" height="16" viewBox="0 0 24 24"><path fill="#bbb" d="M12 21l-1.5-1.3C5 15 2 12.2 2 8.5 2 5.4 4.4 3 7.5 3c1.7 0 3.4.8 4.5 2.1C13.1 3.8 14.8 3 16.5 3 19.6 3 22 5.4 22 8.5c0 3.7-3 6.5-8.5 11.2z"/></svg></div>
      <div><svg width="16" height="16" viewBox="0 0 24 24"><path d="M4 8h14l-3-3M20 16H6l3 3" fill="none" stroke="#999" stroke-width="2"/></svg></div>
      <div><svg width="16" height="16" viewBox="0 0 24 24"><circle cx="12" cy="12" r="8" fill="none" stroke="#999" stroke-width="2"/><path d="M12 8v5" stroke="#999" stroke-width="2"/></svg></div>
    </div>
  </div>
  <div class="abs a-card" style="left:607px">
    <div class="img" role="img" aria-label="Folded crimson scarf with flower beads" style="background:linear-gradient(135deg,#ececf0,#a3122e 40%,#8a0f26 70%,#ececf0)"></div>
    <div class="name">Lorem ipsum dolor</div>
    <div class="price"><s>$160.00</s>$ 150.00</div>
    <div class="actions">
      <div class="buy"><svg width="18" height="18" viewBox="0 0 24 24"><path fill="#fff" d="M7 18a2 2 0 1 0 0 4 2 2 0 0 0 0-4zm10 0a2 2 0 1 0 0 4 2 2 0 0 0 0-4zM5.2 4H2V2h4.5l.9 2H21l-3.2 8H8.4l-.9 2H19v2H4.3l2.3-4.6z"/></svg></div>
      <div><svg width="16" height="16" viewBox="0 0 24 24"><path fill="#bbb" d="M12 21l-1.5-1.3C5 15 2 12.2 2 8.5 2 5.4 4.4 3 7.5 3c1.7 0 3.4.8 4.5 2.1C13.1 3.8 14.8 3 16.5 3 19.6 3 22 5.4 22 8.5c0 3.7-3 6.5-8.5 11.2z"/></svg></div>
      <div><svg width="16" height="16" viewBox="0 0 24 24"><path d="M4 8h14l-3-3M20 16H6l3 3" fill="none" stroke="#999" stroke-width="2"/></svg></div>
      <div><svg width="16" height="16" viewBox="0 0 24 24"><circle cx="12" cy="12" r="8" fill="none" stroke="#999" stroke-width="2"/><path d="M12 8v5" stroke="#999" stroke-width="2"/></svg></div>
    </div>
  </div>

  <div class="abs promo" role="img" aria-label="Model in a red sequin dress beside a white van">
    <div class="abs best">BEST OFFERS</div>
    <div class="abs badge">FLAT<br>20% OFF</div>
  </div>

  <section class="abs testimonials">
    <h2>Testimonials</h2>
    <div class="abs quote" style="left:114px">
      <div class="avatar" role="img" aria-label="Customer portrait in a black hijab" style="background:linear-gradient(#cfd0d6,#2a2a2e)"></div>
      <div class="body">
        <span class="mark" style="left:0;top:-6px">“</span>
        <p>Lorem Ipsum has been the industry's standard dummy text ever since the 1500s, when an unknown printer took a galley of type and scrambled it to make</p>
        <span class="mark" style="right:0;top:48px">”</span>
        <div class="who">Amira Hassan</div>
        <div class="role">Marketing Executive</div>
      </div>
    </div>
    <div class="abs quote" style="left:660px">
      <div class="avatar" role="img" aria-label="Customer portrait in a purple hijab" style="background:linear-gradient(#d8d8de,#4a2a5c)"></div>
      <div class="body">
        <span class="mark" style="left:0;top:-6px">“</span>
        <p>Lorem Ipsum has been the industry's standard dummy text ever since the 1500s, when an unknown printer took a galley of type and scrambled it to make</p>
        <span class="mark" style="right:0;top:48px">”</span>
        <div class="who">Amira Hassan</div>
        <div class="role">Marketing Executive</div>
      </div>
    </div>
  </section>

  <footer class="abs footer">
    <div class="col" style="left:87px">
      <h4>Company</h4>
      <ul><li>About Us</li><li>Privacy Policy</li><li>Terms and Conditions</li><li>Sitemap</li></ul>
    </div>
    <div class="col" style="left:355px">
      <h4>Help</h4>
      <ul><li>Orders and Returns</li><li>Shipping Info</li><li>FAQ</li></ul>
    </div>
    <div class="col info" style="left:605px">
      <h4>Get In Touch</h4>
      <div>Address : 1450 Harbor Lane Ave,<br>Crestwood Bay, NJ</div>
      <div style="margin-top:12px">Phone : 201 555 0187</div>
      <div style="margin-top:12px">Email : hello@qmradiance.com</div>
    </div>
    <div class="col newsletter" style="left:906px">
      <h4>Newsletter</h4>
      <p>Your about us information would fit here nicely.</p>
      <div class="form"><div class="field">Email address</div><div class="submit">Submit</div></div>
      <div class="social"><span></span><span></span><span></span></div>
    </div>
  </footer>

  <div class="abs base">
    <div class="abs cards"><span></span><span></span><span></span><span></span><span></span></div>
    <div class="abs copy">Copyright © 2016. All Rights Reserved</div>
  </div>

</div>
</body>
</html>
```